Willow Glow & Laser - Business Banner with Brand Elements

Design:
• We would like to get a creative design for a wide banner that will go outside our medical spa clinic location. We need a designer to make a simple yet colorful and high-quality design layout. We want this banner to be eye-catching and to communicate the services we offer at our business: Laser Hair Removal | Velonix | Lip Filler.

Requirements:
• We would like the banner to include our companies information which is the following:

Logo
“Refresh Your Skin”
Laser Hair Removal | Velonix | Lip Filler
(555) 287-1936
www.WillowGlowLaser.com

Colors:
• Our business colors are orange, a hint of black and white, but mostly peach/orange tones. (Orange: #f78f20 , White: #ffffff)

Fonts:
• Josefins Sans Bold & Lato

Content and images can be located here:
https://files.cloudvaultshare.com/folders/7tQmZ2xVbR9kLpN4sW8yH3cD6fJ1gA0eU?usp=sharing

The following will give you an idea of our brand presentation:
• Our website is: www.WillowGlowLaser.com
• Our Instagram; @willowglowlaser
• Our Facebook: www.socialpagehub.com/willowglowlaser

Target Market(s)
• Women 25 - 45

Industry/Entity Type
• Beauty

```html
<!DOCTYPE html>
<html lang="en">
<head>
<meta charset="utf-8">
<title>Willow Glow &amp; Laser – Banners</title>
<link rel="stylesheet" href="https://fonts.googleapis.com/css2?family=Josefin+Sans:wght@700&family=Lato:wght@400;700;900&display=swap">
<style>
  :root {
    --orange: #f78f20;
    --white: #ffffff;
    --ink: #2b2b2b;
    --stage: #262626;
    --photo-warm-a: #d9a488;
    --photo-warm-b: #8a6a5c;
    --photo-sea-a: #5fc4d6;
    --photo-sea-b: #efe3cf;
  }
  * { box-sizing: border-box; margin: 0; padding: 0; }
  html, body { width: 1153px; height: 1200px; overflow: hidden; background: var(--stage); }
  .board { position: relative; width: 1153px; height: 1200px; }
  .banner {
    position: absolute; left: 122px; width: 909px; height: 346px; overflow: hidden;
    box-shadow: 0 14px 30px rgba(0,0,0,.45);
    font-family: "Lato", sans-serif;
  }
  .banner--light { top: 188px; background: var(--white); }
  .banner--bold { top: 624px; background: var(--orange); }
  .banner__art { position: absolute; inset: 0; width: 909px; height: 346px; }
  .brand {
    position: absolute; top: 22px; right: 18px; display: flex; align-items: center; gap: 7px;
    font-family: "Lato", sans-serif; font-weight: 900; font-size: 23px; color: var(--ink);
  }
  .brand__dot { width: 30px; height: 30px; border-radius: 50%; background: var(--orange); }

  /* light banner */
  .light__kicker {
    position: absolute; top: 60px; left: 0; width: 370px; text-align: center;
    color: var(--orange); font-size: 23px; letter-spacing: 7px; font-weight: 400;
  }
  .light__title {
    position: absolute; top: 84px; left: 0; width: 370px; text-align: center;
    color: var(--orange); font-size: 50px; font-weight: 700; line-height: 1;
  }
  .light__services {
    position: absolute; top: 143px; left: 30px; width: 286px; height: 65px;
    border: 1.5px solid var(--orange); color: var(--orange);
    font-weight: 700; font-size: 23px; line-height: 27px; text-align: center; padding-top: 4px;
    letter-spacing: -.3px;
  }
  .light__phone {
    position: absolute; top: 237px; left: 42px; color: var(--orange);
    font-weight: 700; font-size: 36px;
  }
  .light__url {
    position: absolute; top: 285px; left: 49px; color: var(--orange); font-size: 20px;
  }

  /* bold banner */
  .bold__title {
    position: absolute; top: 53px; left: 30px; color: var(--ink);
    font-family: "Josefin Sans", sans-serif; font-weight: 700; font-size: 50px; letter-spacing: .5px;
  }
  .bold__services {
    position: absolute; top: 112px; left: 32px; width: 291px; height: 75px;
    border: 1.5px solid var(--white); color: var(--white);
    font-weight: 700; font-size: 29px; line-height: 36px; padding: 1px 0 0 9px;
  }
  .bold__phone-label {
    position: absolute; top: 225px; left: 34px; width: 125px; height: 32px; color: var(--white);
    font-family: "Josefin Sans", sans-serif; font-weight: 700; font-size: 21px;
    line-height: 34px; padding-left: 24px;
  }
  .bold__phone {
    position: absolute; top: 222px; left: 176px; height: 38px; color: var(--orange);
    font-weight: 700; font-size: 32px; line-height: 38px;
  }
  .bold__url {
    position: absolute; top: 273px; left: 34px; color: var(--white); font-size: 27px;
  }
</style>
</head>
<body>
<main class="board">

  <section class="banner banner--light">
    <svg class="banner__art" viewBox="0 0 909 346">
      <defs>
        <linearGradient id="clinicPhoto" x1="0" y1="0" x2="1" y2="1">
          <stop offset="0" stop-color="#d9a488"/>
          <stop offset="1" stop-color="#8a6a5c"/>
        </linearGradient>
      </defs>
      <path d="M393,0 Q330,180 362,346 L909,346 L909,0 Z" fill="#f78f20"/>
      <path d="M431,0 Q342,190 378,346 L909,346 L909,0 Z" fill="url(#clinicPhoto)"
            role="img" aria-label="Photo: smiling client in protective glasses receiving laser hair removal from a technician in the clinic"/>
    </svg>
    <p class="light__kicker">REFRESH</p>
    <h2 class="light__title">YOUR SKIN</h2>
    <p class="light__services">LASER HAIR REMOVAL<br>| VELONIX | LIP FILLER</p>
    <p class="light__phone">(555) 287-1936</p>
    <p class="light__url">www.WillowGlowLaser.com</p>
    <div class="brand"><span class="brand__dot"></span>Willow Glow</div>
  </section>

  <section class="banner banner--bold">
    <svg class="banner__art" viewBox="0 0 909 346">
      <defs>
        <linearGradient id="beachPhoto" x1="0" y1="0" x2="0" y2="1">
          <stop offset="0" stop-color="#5fc4d6"/>
          <stop offset="1" stop-color="#efe3cf"/>
        </linearGradient>
      </defs>
      <polygon points="492,0 504,0 443,346 428,346" fill="#ffffff"/>
      <polygon points="504,0 909,0 909,346 443,346" fill="url(#beachPhoto)"
               role="img" aria-label="Photo: smiling woman in a white bikini lying on the sand by turquoise sea"/>
      <polygon points="43,225 166,225 156,257 33,257" fill="#2b2b2b"/>
      <polygon points="172,222 474,222 468,260 164,260" fill="#ffffff"/>
    </svg>
    <h2 class="bold__title">Refresh Your Skin</h2>
    <p class="bold__services">Laser Hair Removal<br>| Velonix | Lip Filler</p>
    <p class="bold__phone-label">PHONE</p>
    <p class="bold__phone">(555) 287-1936</p>
    <p class="bold__url">www.WillowGlowLaser.com</p>
    <div class="brand"><span class="brand__dot"></span>Willow Glow</div>
  </section>

</main>
</body>
</html>
```